Dr. Lumora needs a design for its website!

*Only need the design, coding is not required.
*Need desktop version ($500) and mobile/tablet version ($200)
*The attached files are not the exact layout we want, they are just for you to know what information should be included in those pages.
*The function of our website is like www.qavlo.hk
*For the background picture, prefer a lively picture and chinese people in it, NOT necessarily need a doctor or sick person in the picture

***Don't just copy the layout from the attachments or from the reference website, we are looking for creative ideas, non-ordinary designs!!!****

We are developing a website for the public to search a doctor by different criteria. At the initial stage, we need 4 pages to start with and other pages at later stage. I have attached the general idea of these pages but not necessarily to be exactly the same, I am looking for some new ideas.

This website needs a professional, modern, simple and user friendly design. The main color to be used in the website will be same as the color (R:0 G:139 B:205) used in our logo (see attached). We don't have any particular thoughts for the other color and the font to be used in the website. Can try to use circle outline for the icon in the navigation bar.

1. Home: will include 4 sections (see attached)

2. Doctor's details (see attached)

3. Health information: will include a short descriptions of this Health Info page and 5 sections (see attached)

4. News (see attached)

Reason: Not too many suitable designs to choose from and need more time to go through the designs

All

Medical

4 page

• must not be same as or looks too much like www.qavlo.hk
• prefer not to use black and red color

```html
<!DOCTYPE html>
<html lang="en">
<head>
<meta charset="utf-8">
<title>Dr. Lumora – Home</title>
<link href="https://fonts.googleapis.com/css2?family=Source+Sans+3:wght@400;600;700&display=swap" rel="stylesheet">
<style>
:root{
  --brand:#008bcd;
  --brand-dark:#1570a6;
  --brand-light:#21a9ec;
  --text:#5a5a5a;
  --text-dark:#333;
  --field:#efefef;
  --field-border:#d6d6d6;
  --chat:#ffcf0a;
  --legal-bar:#e3e3e3;
  --alert:#f0656b;
  --social:#a9a9a9;
  --white:#fff;
}
*{box-sizing:border-box;margin:0;padding:0}
html,body{width:1165px;height:1200px;overflow:hidden}
body{position:relative;background:var(--white);font-family:"Source Sans 3",Arial,sans-serif;color:var(--text)}
.abs{position:absolute}

/* header */
.brand{left:65px;top:42px;display:flex;align-items:center;gap:10px}
.brand-dot{width:44px;height:44px;border-radius:50%;background:var(--brand)}
.brand-name{font-size:30px;font-weight:600;color:var(--brand)}
.utility{right:89px;top:96px;display:flex;align-items:center;font-size:15px;color:var(--text)}
.utility .caret{width:0;height:0;border-left:6px solid transparent;border-right:6px solid transparent;border-top:7px solid #555;margin-right:12px}
.utility .flag{width:30px;height:20px;background:#1d3a8a;margin-right:12px}
.utility .sep{width:1px;height:20px;background:#999;margin:0 11px}

/* nav */
.nav{left:0;top:132px;width:1165px;height:52px;background:var(--brand)}
.nav-item{top:0;height:52px;line-height:52px;color:var(--white);font-size:16px;font-weight:600;text-transform:uppercase}
.nav-item.active{left:43px;width:97px;background:var(--brand-light);text-align:center}
.search{left:792px;top:9px;width:282px;height:34px;border-radius:17px;background:var(--white);padding-left:22px;line-height:34px;color:#b5b5b5;font-size:17px}
.search svg{position:absolute;right:12px;top:8px}

/* hero */
.hero{left:0;top:184px;width:1165px;height:732px;background:radial-gradient(ellipse at 70% 45%,#e7dccf 0%,#eee9e3 40%,#f4f3f1 75%,#f7f7f7 100%)}
.hero-title{left:0;top:232px;width:1165px;text-align:center;font-size:38px;font-weight:700;color:var(--brand-dark)}
.perk{font-size:23px;font-weight:600;color:var(--brand-dark);display:flex;align-items:center;gap:8px;text-transform:uppercase}
.perk svg{flex:none}

.card{background:var(--white);border:1px solid #ddd;border-radius:14px}
.field-label{font-size:17px;color:var(--text)}
.field{height:38px;background:var(--field);border:1px solid var(--field-border)}
.btn{height:38px;border-radius:10px;background:var(--brand);color:var(--white);font-size:17px;font-weight:600;text-align:center;line-height:38px}
.btn.light{background:var(--brand-light)}
.login-title{font-size:21px;color:var(--text);text-align:center;font-weight:600}
.forgot{font-size:16px;color:var(--alert)}

.live-chat{left:1099px;top:495px;width:66px;height:169px;background:var(--chat);border-radius:10px 0 0 10px}
.live-chat span{position:absolute;left:50%;top:50%;transform:translate(-50%,-50%) rotate(-90deg);white-space:nowrap;color:var(--white);font-weight:700;font-size:22px}

/* footer */
.foot-heading{top:968px;font-size:16px;font-weight:600;color:var(--text-dark);text-transform:uppercase}
.foot-list{top:1003px;font-size:14px;line-height:17px;color:var(--text)}
.email-field{left:489px;top:1008px;width:230px;height:39px;background:var(--field);border:1px solid var(--field-border);padding-left:16px;line-height:37px;color:#aaa;font-size:16px}
.social{top:1011px;width:30px;height:30px;border-radius:50%;background:var(--social)}
.social.active{background:var(--brand-dark)}
.legal-bar{left:0;top:1129px;width:1165px;height:36px;background:var(--legal-bar);font-size:13px;color:#666}
.legal-bar span{position:absolute;top:10px}
.legal-bar .sep{left:577px;top:7px;width:1px;height:22px;background:#999}
.copyright{left:0;top:1165px;width:1165px;height:35px;background:var(--brand);color:var(--white);font-size:13px;text-align:center;line-height:35px}
</style>
</head>
<body>

<header>
  <div class="abs brand"><span class="brand-dot"></span><span class="brand-name">Dr. Lumora</span></div>
  <div class="abs utility">
    <span class="caret"></span><span class="flag"></span><span>English</span>
    <span class="sep"></span><span>Customer Support</span>
    <span class="sep"></span><span>Call Us 888-507316</span>
  </div>
</header>

<nav class="abs nav">
  <span class="abs nav-item active">Home</span>
  <span class="abs nav-item" style="left:166px">Doctor List</span>
  <span class="abs nav-item" style="left:287px">Health Info</span>
  <span class="abs nav-item" style="left:430px">News</span>
  <span class="abs nav-item" style="left:537px">About Us</span>
  <span class="abs nav-item" style="left:647px">Contact Us</span>
  <div class="abs search">Search
    <svg width="18" height="18" viewBox="0 0 18 18"><circle cx="7.5" cy="7.5" r="6" fill="none" stroke="#222" stroke-width="2"/><line x1="12" y1="12" x2="16.5" y2="16.5" stroke="#222" stroke-width="2.2" stroke-linecap="round"/></svg>
  </div>
</nav>

<section>
  <div class="abs hero" role="img" aria-label="Soft-focus lifestyle photo of a smiling man talking with a woman"></div>
  <h1 class="abs hero-title">BECOME A DR. LUMORA MEMBER</h1>

  <div class="abs perk" style="left:239px;top:290px"><svg width="24" height="18" viewBox="0 0 24 18"><path d="M2 9l7 7L22 2" fill="none" stroke="currentColor" stroke-width="3"/></svg>First-hand health news</div>
  <div class="abs perk" style="left:239px;top:327px"><svg width="24" height="18" viewBox="0 0 24 18"><path d="M2 9l7 7L22 2" fill="none" stroke="currentColor" stroke-width="3"/></svg>Exclusive prommotions</div>
  <div class="abs perk" style="left:239px;top:364px"><svg width="24" height="18" viewBox="0 0 24 18"><path d="M2 9l7 7L22 2" fill="none" stroke="currentColor" stroke-width="3"/></svg>Instant health advices</div>
  <div class="abs perk" style="left:569px;top:290px"><svg width="24" height="18" viewBox="0 0 24 18"><path d="M2 9l7 7L22 2" fill="none" stroke="currentColor" stroke-width="3"/></svg>Free health seminars / talks</div>
  <div class="abs perk" style="left:569px;top:327px"><svg width="24" height="18" viewBox="0 0 24 18"><path d="M2 9l7 7L22 2" fill="none" stroke="currentColor" stroke-width="3"/></svg>Priority doctor appointments</div>

  <form class="abs card doctor-search" style="left:60px;top:457px;width:474px;height:410px">
    <span class="abs field-label" style="left:30px;top:30px">Doctor’s Name</span><span class="abs field" style="left:180px;top:20px;width:270px"></span>
    <span class="abs field-label" style="left:30px;top:82px">Gender</span><span class="abs field" style="left:180px;top:72px;width:270px"></span>
    <span class="abs field-label" style="left:30px;top:134px">Specialism</span><span class="abs field" style="left:180px;top:124px;width:270px"></span>
    <span class="abs field-label" style="left:30px;top:186px">Symptoms</span><span class="abs field" style="left:180px;top:177px;width:270px"></span>
    <span class="abs field-label" style="left:30px;top:239px">District</span><span class="abs field" style="left:180px;top:229px;width:270px"></span>
    <span class="abs field-label" style="left:30px;top:291px">Phone Number</span><span class="abs field" style="left:180px;top:282px;width:270px"></span>
    <span class="abs btn light" style="left:180px;top:346px;width:120px">Reset</span>
    <span class="abs btn" style="left:330px;top:346px;width:120px">Search</span>
  </form>

  <form class="abs card member-login" style="left:576px;top:620px;width:473px;height:247px">
    <div class="abs login-title" style="left:0;top:25px;width:473px">MEMBER LOGIN</div>
    <span class="abs field-label" style="left:42px;top:79px">Login Email</span><span class="abs field" style="left:158px;top:70px;width:270px"></span>
    <span class="abs field-label" style="left:42px;top:132px">Password</span><span class="abs field" style="left:158px;top:123px;width:270px"></span>
    <span class="abs forgot" style="left:156px;top:185px">Forgot password ?</span>
    <span class="abs btn" style="left:309px;top:179px;width:120px">Login</span>
  </form>

  <div class="abs live-chat"><span>LIVE CHAT</span></div>
</section>

<footer>
  <h3 class="abs foot-heading" style="left:72px">Dr.Lumora.com</h3>
  <div class="abs foot-list" style="left:72px">About Us<br>News<br>Career<br>Partner</div>

  <h3 class="abs foot-heading" style="left:283px">Contact</h3>
  <div class="abs foot-list" style="left:283px">help@drlumora.com<br>888-507316<br><br>18 Harlow Street Floor 3<br>Redfield, CA 94870</div>

  <h3 class="abs foot-heading" style="left:489px">Special Offers</h3>
  <div class="abs email-field">enter email address</div>
  <span class="abs btn" style="left:729px;top:1008px;width:122px;height:39px">Subscribe</span>

  <h3 class="abs foot-heading" style="left:900px">Connect With Us</h3>
  <span class="abs social" style="left:921px"></span>
  <span class="abs social active" style="left:959px"></span>
  <span class="abs social" style="left:994px"></span>

  <div class="abs legal-bar">
    <span style="left:477px">TERM OF USE</span>
    <span class="sep"></span>
    <span style="left:598px">PRIVACY POLICY</span>
  </div>
  <div class="abs copyright">Copyright 2016, Dr.Lumora.com</div>
</footer>

</body>
</html>
```